Harbourline Estate Group

The card is to be black

On the front it will say "Harbourline"
And just under it in smaller writing "Property Group" in dark brown or rose gold

Daniel Forsett
0471 586 209
Admin@harblinegroup.example

On the back it is to say Harbourline Estate group same style as the front but smaller.
And then under that say:
Electrical
General Maintenance
Building works & construction
Energy Consulants

Target Market(s)

Re

Industry/Entity Type

Electrical

Contact Information for Business Card

The card is to be black

Daniel Forsett
0471 586 209
Admin@harblinegroup.example

And then under that say:
Electrical
General Maintenance
Energy Consulants

And somewhere else put residential domestic and industrial

Font styles to use
Serif

Requirements
Should not have
• No pictures of tools etc just a plain sleek card

```html
<!DOCTYPE html>
<html lang="en">
<head>
<meta charset="utf-8">
<title>Harbourline Estate Group – Business Card</title>
<link href="https://fonts.googleapis.com/css2?family=Oswald:wght@600&family=Lato:wght@400;700&display=swap" rel="stylesheet">
<style>
  :root {
    --stage: #2a2a2c;
    --card-dark: #1f1f21;
    --card-dark-2: #2b2b2e;
    --card-light: #e6e6e6;
    --skyline: #cfcfcf;
    --ink-light: #e9e9e9;
    --ink-dark: #1e1e1e;
    --rose: #c0727c;
    --rose-soft: #d7959d;
  }
  * { margin: 0; padding: 0; box-sizing: border-box; }
  html, body { width: 1200px; height: 997px; overflow: hidden; }
  body {
    background: var(--stage);
    font-family: "Lato", sans-serif;
    display: flex;
    flex-direction: column;
    align-items: center;
    justify-content: center;
    gap: 44px;
  }
  .card {
    position: relative;
    width: 760px;
    height: 432px;
    border-radius: 22px;
    overflow: hidden;
    box-shadow: 0 14px 30px rgba(0,0,0,.45);
  }
  .card--front {
    background: linear-gradient(135deg, var(--card-dark-2), var(--card-dark) 60%);
  }
  .wordmark { text-align: center; }
  .wordmark__name {
    font-family: "Oswald", sans-serif;
    font-weight: 600;
    color: var(--ink-light);
    letter-spacing: 1px;
    line-height: 1;
  }
  .wordmark__tagline {
    font-family: "Lato", sans-serif;
    font-weight: 700;
    color: var(--rose);
    letter-spacing: 7px;
    text-transform: uppercase;
  }
  .card--front .wordmark {
    position: absolute;
    top: 82px;
    left: 0; right: 0;
  }
  .card--front .wordmark__name { font-size: 74px; }
  .card--front .wordmark__tagline { font-size: 20px; margin-top: 8px; }

  .front-details {
    position: absolute;
    top: 250px;
    left: 0; right: 0;
    display: flex;
    justify-content: center;
    align-items: flex-end;
  }
  .person { text-align: right; padding-right: 30px; padding-bottom: 4px; }
  .person__name {
    font-weight: 700;
    font-size: 20px;
    color: var(--ink-light);
    text-transform: uppercase;
    letter-spacing: 1px;
  }
  .person__role { font-size: 17px; color: var(--rose); margin-top: 2px; }
  .divider {
    width: 2px;
    height: 118px;
    background: linear-gradient(var(--rose), rgba(192,114,124,0));
  }
  .contact { list-style: none; padding-left: 30px; }
  .contact li {
    display: flex;
    align-items: center;
    gap: 10px;
    font-size: 17px;
    color: var(--ink-light);
    margin: 6px 0;
  }
  .contact svg { width: 16px; height: 16px; fill: var(--rose); }
  .contact .contact__web { color: var(--rose); font-weight: 700; padding-left: 26px; }

  .card--back { background: var(--card-light); }
  .back-top {
    position: absolute;
    inset: 0 0 auto 0;
    height: 210px;
    background: linear-gradient(135deg, var(--card-dark-2), var(--card-dark) 60%);
  }
  .card--back .wordmark {
    position: absolute;
    top: 44px;
    left: 0; right: 0;
  }
  .card--back .wordmark__name { font-size: 52px; }
  .card--back .wordmark__tagline { font-size: 15px; margin-top: 6px; letter-spacing: 6px; }
  .skyline {
    position: absolute;
    top: 150px;
    left: 0; right: 0;
    height: 90px;
    background: linear-gradient(var(--card-dark) 0%, var(--skyline) 100%);
  }
  .services {
    position: absolute;
    top: 262px;
    left: 60px; right: 60px;
  }
  .services__heading {
    display: flex;
    align-items: center;
    gap: 18px;
    font-weight: 700;
    font-size: 21px;
    color: var(--ink-dark);
    text-transform: uppercase;
    letter-spacing: .5px;
  }
  .services__heading::before,
  .services__heading::after {
    content: "";
    flex: 1;
    height: 2px;
    background: var(--rose-soft);
  }
  .services__list {
    list-style: none;
    display: grid;
    grid-template-columns: 1fr 1fr;
    gap: 10px 40px;
    margin: 26px 0 0 60px;
  }
  .services__list li {
    font-size: 19px;
    color: var(--ink-dark);
    display: flex;
    align-items: center;
    gap: 12px;
  }
  .services__list li::before {
    content: "";
    width: 7px; height: 7px;
    border-radius: 50%;
    background: var(--rose);
  }
</style>
</head>
<body>
  <section class="card card--front">
    <div class="wordmark">
      <div class="wordmark__name">HARBOURLINE</div>
      <div class="wordmark__tagline">Property Group</div>
    </div>
    <div class="front-details">
      <div class="person">
        <div class="person__name">Daniel Forsett</div>
        <div class="person__role">Director</div>
      </div>
      <div class="divider"></div>
      <ul class="contact">
        <li>
          <svg viewBox="0 0 24 24" aria-hidden="true"><path d="M6.6 10.8a15.1 15.1 0 0 0 6.6 6.6l2.2-2.2c.3-.3.7-.4 1-.2 1.1.4 2.3.6 3.6.6.6 0 1 .4 1 1V20c0 .6-.4 1-1 1A17 17 0 0 1 3 4c0-.6.4-1 1-1h3.5c.6 0 1 .4 1 1 0 1.3.2 2.5.6 3.6.1.3 0 .7-.2 1z"/></svg>
          0471 586 209
        </li>
        <li>
          <svg viewBox="0 0 24 24" aria-hidden="true"><path d="M2 5h20v14H2zm2 2v.5l8 5 8-5V7l-8 5z"/></svg>
          Admin@harblinegroup.example
        </li>
        <li class="contact__web">www.harblinegroup.example</li>
      </ul>
    </div>
  </section>

  <section class="card card--back">
    <div class="back-top"></div>
    <div class="skyline" role="img" aria-label="City skyline silhouette with harbour bridge"></div>
    <div class="wordmark">
      <div class="wordmark__name">HARBOURLINE</div>
      <div class="wordmark__tagline">Property Group</div>
    </div>
    <div class="services">
      <h2 class="services__heading">Our Services</h2>
      <ul class="services__list">
        <li>Electrical</li>
        <li>Energy Consulants</li>
        <li>General Maintenance</li>
        <li>Building works &amp; construction</li>
      </ul>
    </div>
  </section>
</body>
</html>
```